Customizable Gift Note Card Design

I need a gift note card designed for my Healthy Snacks Care Package company. I need to be able to customize each card with the customer's gift message to the recipient and print to a standard printer.

The card should be single-sided 5 x 7, include our logo, keep colors and graphics simple since they will be printed for each individual order on a standard printer. I would like the following quote to be included in a small and subtle way: "Food is symbolic of love when words are inadequate." —Bertram K. Osslund. Our website thebrightpantrybites.example should also be included.

I have included pictures of our product packaging for reference.

Target Market(s)

Gift recipients: Students, people recovering from illness, housewarming, thank you gifts...etc.

Industry/Entity Type

It Company

Colors

Designer to choose colors to be used in the design.

Requirements
Must have
• We are looking for a simple, cute and elegant gift card that reflects our branding. Must be customizable and printable on a standard printer.
• Must be single-sided 5x7.

```html
<!DOCTYPE html>
<html lang="en">
<head>
<meta charset="utf-8">
<title>Gift Note Card – The Bright Pantry</title>
<link rel="stylesheet" href="https://fonts.googleapis.com/css2?family=Raleway:ital,wght@0,300;0,400;1,300&display=swap">
<style>
  :root {
    --paper: #fbf3ec;
    --lace-light: #f3e6dd;
    --lace-mid: #ecdcd1;
    --lace-band: #e6d2c6;
    --ink: #8b8580;
    --ink-soft: #9d9791;
    --brand-dot: #c9b3a6;
  }
  * { margin: 0; padding: 0; box-sizing: border-box; }
  html, body {
    width: 880px;
    height: 1200px;
    overflow: hidden;
    background: var(--paper);
  }
  .card {
    position: relative;
    width: 880px;
    height: 1200px;
    background: var(--paper);
    font-family: "Raleway", sans-serif;
    color: var(--ink);
  }
  .lace-field {
    position: absolute;
    left: 0; top: 0;
    width: 880px;
    height: 915px;
    background: radial-gradient(ellipse at 50% 40%, var(--lace-light) 0%, var(--paper) 75%);
  }
  .lace-trim {
    position: absolute;
    left: 0; top: 915px;
    width: 880px;
    height: 95px;
    background: linear-gradient(to bottom, var(--lace-light) 0%, var(--lace-band) 55%, var(--lace-mid) 100%);
  }
  .quote {
    position: absolute;
    left: 32px;
    top: 1052px;
    font-weight: 300;
    font-size: 19px;
    line-height: 1.3;
    color: var(--ink);
  }
  .quote__author {
    display: block;
    margin-top: 16px;
    padding-left: 14px;
    font-style: italic;
  }
  .brand {
    position: absolute;
    right: 32px;
    top: 1060px;
    display: flex;
    flex-direction: column;
    align-items: center;
  }
  .brand__dot {
    width: 54px;
    height: 54px;
    border-radius: 50%;
    background: var(--brand-dot);
  }
  .brand__name {
    margin-top: 8px;
    font-weight: 400;
    font-size: 17px;
    color: var(--ink);
  }
  .website {
    position: absolute;
    right: 32px;
    top: 1148px;
    font-weight: 400;
    font-size: 19px;
    color: var(--ink-soft);
  }
</style>
</head>
<body>
  <main class="card">
    <div class="lace-field" role="img" aria-label="Faint floral lace pattern covering the writing area of the card"></div>
    <div class="lace-trim" role="img" aria-label="Scalloped lace trim band across the card"></div>

    <p class="quote">
      Food is symbolic of love<br>when words are inadequate.
      <span class="quote__author">- Bertram K. Osslund</span>
    </p>

    <div class="brand">
      <span class="brand__dot"></span>
      <span class="brand__name">Bright Pantry</span>
    </div>

    <p class="website">thebrightpantrybites.example</p>
  </main>
</body>
</html>
```